Build a landing page to promote a service (dialler consultation and support).

We are a call centre consultation firm and we need a landing page to promote a service. The service is Morvexa dialler consultation and support.
If you do not know what Morvexa is, please do some quick "Zumbrel" research for more information.
The landing page will be promoted with a paid advertisement, so we want something that is simple, and explains exactly what service we offer.
There are two objectives for the landing page:
1) A "call to action" which directs the user to a contact page, including a form plus all of our contact details.
2) A form for them viewers to enter their details to get a "FREE" quote for their project. This form should be placed on the main page.
Notes:
The call to action will require the viewer to enter their name, email, phone number as well as a description of their request. There will also need to be a drop down menu for the type of quote. This menu should have the following options:
1) Morvexa support
2) Morvexa hosting
3) Morvexa customisation
4) Other
We need 2 pages in total:
1) Main landing page
This is the home page. It will need to clearly indicate our services and our key selling features.
Services:
* Morvexa support
* Morvexa hosting
* Morvexa customisation
Key Selling Features:
* Australian based
* PCI complaint
* 10+ years of dialler and call centre experience
* we run a sister company which is a highly reputable 40 seat call centre, so we know first hand about call centre technology.
The main landing page will have an "about us" section with a few paragraphs about how we got started.
-------------------------------------------------------------------------
2) Contact page
All of our contact details will live on this page, as well as a contact form.
Other notes:
We will be self hosting the landing page.
We already have a domain name.
The design must be clean and incorporate our logo, as well as it's colours. (Logo attached)
We want a fully function HTML landing page, not just a "PSD" design.
The page must be mobile optimised.
Anyone using Morvexa software.

```html
<!DOCTYPE html>
<html lang="en">
<head>
<meta charset="utf-8">
<title>Tellvance – Morvexa Dialler Support</title>
<link href="https://fonts.googleapis.com/css2?family=Lato:wght@400;700;900&display=swap" rel="stylesheet">
<style>
:root{
  --blue:#1b78c6;
  --blue-dark:#1664a8;
  --teal:#22aa8c;
  --teal-light:#2cbf9c;
  --ink:#222628;
  --muted:#6b6f72;
  --panel:#f6f9ee;
  --field-border:#d9dfd0;
  --footer:#151719;
  --page:#ffffff;
}
*{box-sizing:border-box;margin:0;padding:0}
html,body{width:1200px;height:3579px;overflow:hidden}
body{background:var(--page);font-family:'Lato',sans-serif;color:var(--ink);position:relative}
.abs{position:absolute}
.section-label{position:absolute;left:0;width:1200px;text-align:center;font-weight:700;font-size:34px;letter-spacing:2px;color:var(--ink)}
.frame{position:absolute;left:53px;width:1099px;overflow:hidden;box-shadow:0 2px 10px rgba(0,0,0,.25);background:#fff}
.frame::before{content:"";position:absolute;left:0;top:0;right:0;height:5px;background:linear-gradient(90deg,var(--blue),var(--teal));z-index:3}
.photo{position:absolute}
.brand{position:absolute;display:flex;align-items:center;gap:10px;font-weight:700;font-size:28px;color:var(--blue);z-index:2}
.brand-dot{width:34px;height:34px;border-radius:50%;background:var(--blue)}
.quote-form{position:absolute;width:331px;background:var(--panel);box-shadow:0 2px 8px rgba(0,0,0,.18);z-index:2}
.quote-form h3{background:linear-gradient(90deg,var(--blue),var(--teal));color:#fff;font-weight:700;font-size:25px;text-align:center;height:58px;line-height:58px}
.fields{padding:26px 19px 0}
.field{height:43px;border:1.5px solid var(--field-border);background:#fff;margin-bottom:17px;font-size:12px;color:var(--muted);padding:13px 12px}
.field.tall{height:77px}
.field.select{display:flex;justify-content:space-between}
.field.select span.arrow{color:var(--blue);font-size:12px}
.submit{display:block;margin:8px auto 0;width:197px;height:43px;background:linear-gradient(90deg,var(--blue),var(--teal));color:#fff;font-weight:700;font-size:20px;text-align:center;line-height:43px}
.footer{position:absolute;left:0;right:0;bottom:0;height:43px;background:var(--footer);color:#ddd;font-size:11px;display:flex;align-items:center;padding:0 70px;z-index:2}
.footer .sep{margin:0 14px}
.footer .ver{margin-left:auto;font-weight:700}
.contact-tab{position:absolute;left:854px;top:4px;width:192px;height:39px;background:var(--teal);color:#fff;font-weight:700;font-size:19px;text-align:center;line-height:39px;z-index:2;clip-path:polygon(0 0,100% 0,100% 100%,8% 100%)}
.nav{position:absolute;display:flex;align-items:center;gap:24px;z-index:2;font-size:16px;color:var(--ink)}
.nav a{text-decoration:none;color:inherit}
.nav .active{background:var(--teal);color:#fff;border-radius:22px;padding:11px 24px}
.services{position:absolute;left:0;top:643px;width:100%;height:468px;background:linear-gradient(90deg,var(--blue),var(--teal))}
.services h2,.about h2{color:#fff;text-align:center;font-weight:700;font-size:36px;padding-top:30px}
.chev{position:absolute;left:535px;top:-12px;width:28px;height:28px;border-radius:50%;background:var(--blue);z-index:3}
.cards{position:absolute;left:67px;top:115px;display:flex;gap:26px}
.card{width:305px;height:300px;background:rgba(255,255,255,.15);text-align:center;color:#fff;padding-top:24px}
.card h4{font-weight:900;font-size:20px}
.card svg{margin:14px auto 10px;display:block}
.card p{font-size:13px;line-height:20px;padding:0 26px}
.pill{display:inline-block;background:var(--teal-light);color:#fff;font-size:15px;border-radius:22px;padding:11px 27px;box-shadow:0 2px 6px rgba(0,0,0,.2)}
.card .pill{margin-top:18px}
.features{position:absolute;left:0;top:1111px;width:100%;height:413px;background:#fff}
.features h2{position:absolute;left:67px;top:65px;font-weight:700;font-size:36px}
.features ul{position:absolute;left:67px;top:134px;width:470px;list-style:none;font-size:14px;line-height:30px}
.features li{position:relative;padding-left:33px}
.features li::before{content:"";position:absolute;left:4px;top:9px;width:11px;height:6px;border-left:2.5px solid var(--teal);border-bottom:2.5px solid var(--teal);transform:rotate(-45deg)}
.features .pill{position:absolute;left:67px;top:298px}
.about{position:absolute;left:0;top:1524px;width:100%;height:307px;background:linear-gradient(90deg,var(--blue),var(--teal));text-align:center}
.about p{color:#fff;font-size:14px;line-height:26px;width:820px;margin:16px auto 24px}
.address-card{position:absolute;left:516px;top:165px;width:285px;height:159px;background:#fff;padding:24px 28px;font-size:17px;line-height:23px;z-index:2;box-shadow:0 2px 6px rgba(0,0,0,.15)}
.address-card .row{display:flex;gap:10px}
.address-card .row + .row{margin-top:20px}
.map-note{position:absolute;right:20px;bottom:50px;font-size:10px;color:#555;z-index:2}
</style>
</head>
<body>

<div class="section-label" style="top:48px">LANDING PAGE</div>
<section class="frame" style="top:106px;height:652px">
  <div class="photo" role="img" aria-label="Smiling call centre agent wearing a headset and glasses, on a bright office background" style="left:0;top:0;width:100%;height:609px;background:linear-gradient(90deg,#f1f3f4 0%,#e6eaec 45%,#8da3b4 70%,#4f6e88 100%)"></div>
  <div class="contact-tab">Contact Us</div>
  <div class="brand" style="left:67px;top:30px"><span class="brand-dot"></span>Tellvance</div>
  <form class="quote-form" style="left:67px;top:129px">
    <h3>Get a Quote "FREE"</h3>
    <div class="fields">
      <div class="field">Name</div>
      <div class="field">Email</div>
      <div class="field">Phone Number</div>
      <div class="field tall">Description</div>
      <div class="field select"><span>Morvexa support</span><span class="arrow">▼</span></div>
    </div>
    <span class="submit">Submit</span>
    <div style="height:0"></div>
  </form>
  <footer class="footer"><span>© 2018</span><span class="sep">|</span><span>www.companyname.com</span><span class="ver">M1</span></footer>
</section>

<div class="section-label" style="top:820px">MAIN HOME PAGE</div>
<section class="frame" style="top:893px;height:1886px">
  <div class="photo" role="img" aria-label="Call centre team working at computers with headsets, smiling agent in the foreground" style="left:0;top:5px;width:100%;height:638px;background:linear-gradient(100deg,#6e7f8d 0%,#c9cfd3 30%,#9aa7b1 55%,#3c4a56 85%,#1f2a33 100%)"></div>
  <div class="brand" style="left:67px;top:22px"><span class="brand-dot"></span>Tellvance</div>
  <nav class="nav" style="left:504px;top:43px">
    <a class="active">Home</a><a>About Us</a><a>Services</a><a>Features</a><a>Contact Us</a>
  </nav>
  <form class="quote-form" style="left:653px;top:158px">
    <h3>Get a Quote "FREE"</h3>
    <div class="fields">
      <div class="field">Name</div>
      <div class="field">Email</div>
      <div class="field">Phone Number</div>
      <div class="field tall">Description</div>
      <div class="field select"><span>Morvexa support</span><span class="arrow">▼</span></div>
    </div>
    <span class="submit">Submit</span>
  </form>

  <section class="services">
    <svg class="chev" viewBox="0 0 28 28"><path d="M8 11l6 6 6-6" fill="none" stroke="#fff" stroke-width="3"/></svg>
    <h2>OUR SERVICES</h2>
    <div class="cards">
      <div class="card">
        <h4>MORVEXA SUPPORT</h4>
        <svg width="70" height="70" viewBox="0 0 70 70" fill="none" stroke="#fff" stroke-width="4"><path d="M14 38V30a21 21 0 0 1 42 0v8"/><rect x="8" y="34" width="10" height="18" rx="3" fill="#fff"/><rect x="52" y="34" width="10" height="18" rx="3" fill="#fff"/><path d="M57 52c0 8-8 11-18 11"/></svg>
        <p>Duis aute irure dolor in reprehenderit in voluptate velit esse cillum dolore eu fugiat nulla pariatur.</p>
        <span class="pill">Read more</span>
      </div>
      <div class="card">
        <h4>MORVEXA HOSTING</h4>
        <svg width="70" height="70" viewBox="0 0 70 70" fill="#fff"><rect x="10" y="14" width="42" height="12" rx="2"/><rect x="10" y="30" width="42" height="12" rx="2"/><rect x="10" y="46" width="42" height="12" rx="2"/><circle cx="58" cy="22" r="7"/><circle cx="58" cy="40" r="7"/></svg>
        <p>Duis aute irure dolor in reprehenderit in voluptate velit esse cillum dolore eu fugiat nulla pariatur.</p>
        <span class="pill">Read more</span>
      </div>
      <div class="card">
        <h4>MORVEXA CUSTOMISATION</h4>
        <svg width="70" height="70" viewBox="0 0 70 70" fill="none" stroke="#fff" stroke-width="4"><circle cx="40" cy="30" r="10"/><circle cx="40" cy="30" r="18" stroke-dasharray="6 5"/><path d="M12 60l20-20"/><path d="M8 56l8 8" /></svg>
        <p>Duis aute irure dolor in reprehenderit in voluptate velit esse cillum dolore eu fugiat nulla pariatur.</p>
        <span class="pill">Read more</span>
      </div>
    </div>
  </section>

  <section class="features">
    <h2>OUR FEATURES</h2>
    <ul>
      <li>Australian based</li>
      <li>PCI complaint</li>
      <li>10+ years of dialler and call centre experience</li>
      <li>we run a sister company which is a highly reputable 40 seat call centre, so we know first hand about call centre technology.</li>
    </ul>
    <span class="pill">Read more</span>
    <div class="photo" role="img" aria-label="Three call centre agents with headsets working at desks" style="left:561px;top:50px;width:471px;height:346px;background:linear-gradient(135deg,#dfe3e6 0%,#b8c0c7 40%,#5b6b78 75%,#2e3a45 100%)"></div>
  </section>

  <section class="about">
    <h2>ABOUT US</h2>
    <p>Sed ut perspiciatis unde omnis iste natus error sit voluptatem accusantium doloremque laudantium, totam rem aperiam, eaque ipsa quae ab illo inventore veritatis et quasi architecto beatae vitae dicta sunt explicabo. Nemo enim ipsam voluptatem quia voluptas sit aspernatur aut odit aut fugit,</p>
    <span class="pill">Read more</span>
  </section>
  <footer class="footer"><span>© 2018</span><span class="sep">|</span><span>www.companyname.com</span><span class="ver">M1</span></footer>
</section>

<div class="section-label" style="top:2822px">CONTACT PAGE</div>
<section class="frame" style="top:2897px;height:655px">
  <div class="photo" role="img" aria-label="Street map of a coastal suburban area showing the office location" style="left:0;top:5px;width:100%;height:607px;background:linear-gradient(120deg,#eceae3 0%,#e3e6dc 45%,#d6dfe6 65%,#a9c8e2 100%)"></div>
  <div class="brand" style="left:67px;top:22px"><span class="brand-dot"></span>Tellvance</div>
  <nav class="nav" style="left:492px;top:30px">
    <a class="active">Home</a><a>About Us</a><a>Services</a><a>Features</a><a>Contact Us</a>
  </nav>
  <form class="quote-form" style="left:67px;top:137px">
    <h3>Contact Form</h3>
    <div class="fields">
      <div class="field">Name</div>
      <div class="field">Email</div>
      <div class="field">Phone Number</div>
      <div class="field tall">Description</div>
    </div>
    <span class="submit" style="background:var(--blue);margin-top:14px">Submit</span>
    <div style="height:30px"></div>
  </form>
  <div class="address-card">
    <div class="row">
      <svg width="16" height="22" viewBox="0 0 16 22"><path d="M8 0a8 8 0 0 0-8 8c0 6 8 14 8 14s8-8 8-14a8 8 0 0 0-8-8z" fill="#222"/><circle cx="8" cy="8" r="3" fill="#fff"/></svg>
      <span>2170 Harbour Lane,<br>Brightwater,<br>NY 11904.</span>
    </div>
    <div class="row">
      <svg width="16" height="22" viewBox="0 0 16 22"><rect x="2" y="1" width="12" height="20" rx="2" fill="#222"/><rect x="4" y="4" width="8" height="12" fill="#fff"/></svg>
      <span>1-800 555 0142</span>
    </div>
  </div>
  <div class="map-note">Map data ©2019 Zumbrel</div>
  <footer class="footer"><span>© 2018</span><span class="sep">|</span><span>www.companyname.com</span><span class="ver">M1</span></footer>
</section>

</body>
</html>
```